Self help book from Bright Harbor needs awesome cover

We need a paperback and e-book cover for a self help book that is about to be published. The title is 'Silver Compass Calls Traveler: Shape Restless Hunger Toward Splendor'. Synopsis: Future You has achieved great success, and is trying to get an urgent communication to Present You to tell you how to master your mind and life so that you can achieve that greatness. If you don’t, the future won’t happen like it can, or should. Your destiny is to really make a difference in the lives of all of us. It’s not just for you. There are practical things you can do to think more clearly, and some mindfulness exercises to hone your skills. We currently do not have any color or graphic preferences, we're excited to see what you come up with! The final cover should express clarity, confidence, and a bit of urgency. Author's name is Glen Marlow. Author name should be at the bottom.

```html
<!DOCTYPE html>
<html lang="en">
<head>
<meta charset="utf-8">
<title>Silver Compass Calls Traveler — Glen Marlow</title>
<link rel="stylesheet" href="https://fonts.googleapis.com/css2?family=Bebas+Neue&family=Cinzel:wght@400;500&display=swap">
<style>
  :root {
    --page: #ffffff;
    --navy-edge: #141d47;
    --navy-mid: #1e3f74;
    --navy-glow: #2062a2;
    --gold-deep: #d8a656;
    --gold-light: #f8e6a2;
    --ink-white: #ffffff;
    --author-ink: #1c2c5c;
  }
  html, body {
    margin: 0;
    width: 1200px;
    height: 1200px;
    overflow: hidden;
    background: var(--page);
  }
  .canvas {
    position: relative;
    width: 1200px;
    height: 1200px;
  }
  .book-cover {
    position: absolute;
    left: 260px;
    top: 91px;
    width: 679px;
    height: 1018px;
    display: block;
  }
  .title-word { font-family: "Bebas Neue", "Arial Narrow", sans-serif; }
  .subtitle-line { font-family: "Cinzel", "Times New Roman", serif; letter-spacing: 2px; }
  .author-name { font-family: "Bebas Neue", "Arial Narrow", sans-serif; }
</style>
</head>
<body>
<main class="canvas">
  <svg class="book-cover" viewBox="0 0 679 1018" xmlns="http://www.w3.org/2000/svg" aria-label="Book cover: Silver Compass Calls Traveler by Glen Marlow">
    <defs>
      <radialGradient id="cover-field" cx="0.5" cy="0.56" r="0.72">
        <stop offset="0" style="stop-color: var(--navy-glow)"/>
        <stop offset="0.55" style="stop-color: var(--navy-mid)"/>
        <stop offset="1" style="stop-color: var(--navy-edge)"/>
      </radialGradient>
      <linearGradient id="gold-sheen" x1="0" y1="0" x2="1" y2="0">
        <stop offset="0" style="stop-color: var(--gold-deep)"/>
        <stop offset="0.5" style="stop-color: var(--gold-light)"/>
        <stop offset="1" style="stop-color: var(--gold-deep)"/>
      </linearGradient>
      <linearGradient id="rule-fade" x1="0" y1="0" x2="1" y2="0">
        <stop offset="0" stop-color="#ffffff" stop-opacity="0"/>
        <stop offset="0.5" stop-color="#ffffff" stop-opacity="1"/>
        <stop offset="1" stop-color="#ffffff" stop-opacity="0"/>
      </linearGradient>
    </defs>

    <rect class="cover-field" x="0" y="0" width="679" height="1018" fill="url(#cover-field)"/>

    <g class="title-block" fill="url(#gold-sheen)">
      <text class="title-word" x="75" y="158" font-size="136" textLength="528" lengthAdjust="spacingAndGlyphs">SILVER</text>
      <text class="title-word" x="74" y="338" font-size="227" textLength="530" lengthAdjust="spacingAndGlyphs">COMPASS</text>
      <text class="title-word" x="77" y="555" font-size="148" textLength="526" lengthAdjust="spacingAndGlyphs">TRAVELER</text>
    </g>

    <g class="title-connector">
      <line x1="80" y1="394" x2="248" y2="394" stroke="url(#rule-fade)" stroke-width="1.5"/>
      <line x1="432" y1="394" x2="602" y2="394" stroke="url(#rule-fade)" stroke-width="1.5"/>
      <text class="title-word" x="340" y="426" font-size="90" fill="var(--ink-white)" text-anchor="middle" textLength="160" lengthAdjust="spacingAndGlyphs">CALLS</text>
    </g>

    <g class="subtitle-block" fill="var(--ink-white)" text-anchor="middle">
      <line x1="112" y1="665" x2="566" y2="665" stroke="url(#rule-fade)" stroke-width="2"/>
      <text class="subtitle-line" x="340" y="720" font-size="38">SHAPE</text>
      <text class="subtitle-line" x="340" y="771" font-size="38">RESTLESS HUNGER</text>
      <text class="subtitle-line" x="340" y="822" font-size="38">TOWARD SPLENDOR</text>
      <line x1="112" y1="847" x2="566" y2="847" stroke="url(#rule-fade)" stroke-width="2"/>
    </g>

    <g class="author-band">
      <rect x="0" y="917" width="679" height="101" fill="url(#gold-sheen)"/>
      <text class="author-name" x="340" y="999" font-size="90" fill="var(--author-ink)" text-anchor="middle" textLength="338" lengthAdjust="spacingAndGlyphs">GLEN MARLOW</text>
    </g>
  </svg>
</main>
</body>
</html>
```